Business Card Design Project

Business Card design based on logo.

I need business card, letterhead, envelope, and if possible, Powerpoint slide template.

On front of business card: Just logo- and  my name and title:  Rosalind Pekar, Principal

On reverse-logo and the rest of the contact info:

4857 Orchard Lane
Fernhollow, CA 95990
650-381-2276
rp@brindlestudyworks.example

On letterhead-Just logo at top, at bottom  the rest-very small along the bottom

On PPT slide-just the logo.

I also want to try a few other colors-I like lime/dark grey (not black) but would like to try Sienna, maybe also indigo or bright blue-green.

I forgot to add-

On the business card-switch to vertical on reverse side and put:

Reverse side-switch to vertical and list:

Rosalind Pekar
Principal
Brindle Study Works, LLC

650-381-2276

4857 Orchard Lane
Fernhollow, CA 95990

Rosalind Pekar
Principal

650-381-2276

4857 Orchard Lane
Fernhollow, CA 95990

I have another project at the same time-for Stationery. Feel free to submit to that one also.

That one includes letterhead, envelope, PPT slide, folder cover sheet-RP

Industry/Entity Type

Business

Requirements
Must have
• Must use logo-preferably lime green version-with gray, not black or just 2-tone -logo on colored background.

```html
<!DOCTYPE html>
<html lang="en">
<head>
<meta charset="utf-8">
<title>Brindle Study Works — Stationery</title>
<link rel="stylesheet" href="https://fonts.googleapis.com/css2?family=PT+Sans:wght@400;700&display=swap">
<style>
  :root{
    --lime:#7cb12a;
    --ink:#1f1f1f;
    --charcoal:#222324;
    --paper:#f5f5f4;
    --backdrop:#e7e7e7;
    --muted:#4a4a4a;
    --on-dark:#e9e9e9;
  }
  *{box-sizing:border-box;margin:0;padding:0}
  html,body{width:1200px;height:900px;overflow:hidden}
  body{background:var(--backdrop);font-family:"PT Sans",Arial,sans-serif;color:var(--ink);position:relative}

  .sheet{position:absolute;background:var(--paper);overflow:hidden}

  /* wordmark */
  .wordmark{display:flex;align-items:center;gap:6px;font-weight:700;color:var(--ink);white-space:nowrap;letter-spacing:.04em;text-transform:uppercase}
  .wordmark .mark{display:block;background:var(--lime)}
  .wordmark.on-dark{color:var(--on-dark)}

  /* letterhead */
  .letterhead{left:113px;top:113px;width:457px;height:648px}
  .letterhead .wordmark{position:absolute;top:92px;left:0;right:0;justify-content:center;font-size:17px}
  .letterhead .wordmark .mark{width:12px;height:12px}
  .letter{position:absolute;left:65px;top:178px;width:335px;font-size:8.4px;line-height:11.2px;color:var(--ink)}
  .letter p{margin-bottom:22px}
  .letter .salutation{margin-bottom:12px}
  .letter .body{margin-bottom:46px}
  .letter .signature{width:62px;height:22px;margin-top:18px;background:linear-gradient(90deg,rgba(48,48,140,.18),rgba(48,48,140,.06));border-radius:3px}
  .letter-footer{position:absolute;left:27px;right:27px;top:614px;font-size:5.4px;color:var(--muted);display:flex;gap:5px;align-items:center;white-space:nowrap}
  .letter-footer .dot{width:4px;height:4px;border-radius:50%;background:var(--lime);display:inline-block}
  .edge-band{position:absolute;left:0;right:0;bottom:0;height:14px;background:var(--charcoal);border-top:2px solid var(--lime)}
  .letterhead .edge-band{height:15px}

  /* envelope back */
  .envelope-back{left:611px;top:114px;width:512px;height:244px}
  .envelope-back .flap{position:absolute;left:0;top:0;right:0;height:87px;background:linear-gradient(180deg,#2b2c2d,#161616);border-radius:0 0 10px 10px;display:flex;align-items:center;justify-content:center}
  .envelope-back .wordmark{font-size:12px;color:var(--lime)}

  /* envelope front */
  .envelope-front{left:611px;top:378px;width:512px;height:245px}
  .envelope-front .wordmark{position:absolute;left:26px;top:74px;font-size:14px}
  .envelope-front .wordmark .mark{width:10px;height:10px}
  .return-address{position:absolute;left:26px;top:107px;font-size:6px;line-height:8.4px;color:var(--muted)}
  .envelope-front .edge-band{height:13px}

  /* cards */
  .card{top:640px;width:116px;height:210px;box-shadow:0 3px 6px rgba(0,0,0,.12)}
  .card-front{left:629px}
  .card-front .wordmark{position:absolute;top:60px;left:0;right:0;justify-content:center;font-size:8.4px;gap:4px}
  .card-front .wordmark .mark{width:6px;height:6px}
  .name-band{position:absolute;left:0;right:0;top:101px;height:31px;background:var(--lime);color:#fff;padding:6px 10px}
  .name-band .name{font-size:7px;font-weight:700;display:block}
  .name-band .title{font-size:5.4px;display:block;margin-top:1px}
  .contact-panel{position:absolute;left:0;right:0;top:132px;bottom:0;background:var(--charcoal);color:var(--on-dark);font-size:4.9px;line-height:7px;padding:13px 10px 0}
  .contact-panel .row{display:flex;gap:5px;align-items:flex-start}
  .contact-panel .row + .row{margin-top:1px}
  .contact-panel .spacer{height:6px}
  .contact-panel .dot{flex:none;width:5px;height:5px;border-radius:50%;background:var(--lime);margin-top:1px}

  .card-back{left:771px;width:115px;background:linear-gradient(180deg,#2a2b2c,#151515)}
  .card-back .wordmark{position:absolute;top:116px;left:0;right:0;justify-content:center;font-size:8.4px;gap:4px}
  .card-back .wordmark .mark{width:6px;height:6px}
  .card-back .web{position:absolute;bottom:27px;left:0;right:0;text-align:center;font-size:5.2px;color:var(--on-dark)}
</style>
</head>
<body>

  <section class="sheet letterhead" aria-label="Letterhead">
    <div class="wordmark"><span class="mark"></span>Brindle Study Works</div>

    <div class="letter">
      <p>Your Street Address<br>Your City, State&nbsp; Zip<br>Date</p>
      <p>First and Last Name of the Person to whom you are writing<br>Their Street Address<br>City, ST Zip</p>
      <p class="salutation">Dear Mr./Ms. Full Name:</p>
      <p class="body">You do not want to indent when you are using this format.&nbsp; This is the best format to use when you are writing a persuasive letter.&nbsp; You want to introduce yourself and the topic you are writing about to the reader.&nbsp; Remember that the first rule of writing is to know your audience.&nbsp; In a persuasive letter, you state your opinion or your feelings about something that is important to you after you have introduced yourself. You must sound as professional and passionate as possible.&nbsp; You do not want to belittle the reader or they will not finish reading your letter.&nbsp; Your letter needs to have the facts, reasons, and examples to support your position. Address issues that your reader may have in their argument.<br>In a second paragraph, you must have solutions.&nbsp; Without solutions, you are only complaining. Offer assistance in solving the problem.&nbsp; Remind the reader where they can contact you.</p>
      <p>Sincerely yours,</p>
      <div class="signature" role="img" aria-label="Handwritten signature"></div>
    </div>

    <div class="letter-footer">
      <span>Brindle Study Works, LLC: 4857 Orchard Lane, Fernhollow, CA 95990</span>
      <span class="dot"></span><span>650-381-2276</span>
      <span class="dot"></span><span>rp@brindlestudyworks.example</span>
      <span class="dot"></span><span>www.brindlestudyworks.example</span>
    </div>
    <div class="edge-band"></div>
  </section>

  <section class="sheet envelope-back" aria-label="Envelope back">
    <div class="flap"><div class="wordmark">Brindle Study Works</div></div>
  </section>

  <section class="sheet envelope-front" aria-label="Envelope front">
    <div class="wordmark"><span class="mark"></span>Brindle Study Works</div>
    <p class="return-address">Brindle Study Works, LLC<br>4857 Orchard Lane, Fernhollow, CA 95990</p>
    <div class="edge-band"></div>
  </section>

  <section class="sheet card card-front" aria-label="Business card front">
    <div class="wordmark"><span class="mark"></span>Brindle Study Works</div>
    <div class="name-band">
      <span class="name">Rosalind Pekar</span>
      <span class="title">Principal</span>
    </div>
    <div class="contact-panel">
      <div class="row"><span class="dot"></span><span>Brindle Study Works, LLC<br>4857 Orchard Lane, Fernhollow, CA 95990</span></div>
      <div class="spacer"></div>
      <div class="row"><span class="dot"></span><span>650-381-2276</span></div>
      <div class="row"><span class="dot"></span><span>rp@brindlestudyworks.example</span></div>
      <div class="row"><span class="dot"></span><span>www.brindlestudyworks.example</span></div>
    </div>
  </section>

  <section class="sheet card card-back" aria-label="Business card back">
    <div class="wordmark on-dark"><span class="mark"></span>Brindle Study Works</div>
    <p class="web">www.brindlestudyworks.example</p>
  </section>

</body>
</html>
```